Pediatric Therapy Clinic Brochure

We need a Brochure for a new pediatric therapy clinic. The clinic offers occupational therapy, physical therapy, speech therapy and feeding therapy. We want a brochure for parents, doctors and medical professional. It should have a fun and inviting, but still professional feel. Should be kid focused, bright and colorful. All the text / wording is there and a rough layout. Now I need someone to tidy and jazz it up and make it look professional.

Target Market(s)

Parents, doctors, medical professional

Industry/Entity Type

Medical

Font styles to use
Serif
Sans Serif

Requirements
Must have
• Keep All the text with information about services the same. Logo on front. Pictures throughout (use any of the pictures provided) (try and match up with corresponding service) (pictures are labeled). Need to have Map and contact info
• Keep colors consistent with our logo
Nice to have
• Background, special effects. Make it look fancy and professional
Should not have
• Not so busy that is takes away from the text

```html
<!DOCTYPE html>
<html lang="en">
<head>
<meta charset="UTF-8">
<title>Pediatric Therapy Brochure – Inside Spread</title>
<link href="https://fonts.googleapis.com/css2?family=Arimo:ital,wght@0,400;0,700;1,400;1,700&display=swap" rel="stylesheet">
<style>
  :root{
    --bg:#c9c9cb;
    --blue:#1f67a3;
    --blue-deep:#174f86;
    --blue-light:#3e8cc6;
    --navy:#1b4f7e;
    --orange:#e2561e;
    --panel-grey:#e9e9ec;
    --text-dark:#1c1c1c;
    --text-muted:#c9dcef;
    --white:#ffffff;
  }
  *{box-sizing:border-box;margin:0;padding:0}
  html,body{width:1200px;height:1200px;overflow:hidden}
  body{background:var(--bg);font-family:"Arimo",Arial,sans-serif;position:relative}
  .brochure{position:absolute;left:30px;top:160px;width:1140px;height:880px;display:flex;box-shadow:0 10px 30px rgba(0,0,0,.25)}
  .panel{position:relative;width:380px;height:880px;overflow:hidden}
  .panel--blue{background:radial-gradient(ellipse at 50% 45%,var(--blue-light),var(--blue) 60%,var(--blue-deep))}
  .photo{position:absolute;display:block}
  .panel-title{font-weight:700;color:var(--white);font-size:27px;line-height:1.1}
  .lead{font-size:13px;line-height:1.4;color:var(--text-muted);margin:6px 0 12px}
  .service-list{list-style:none;font-size:13.5px;line-height:1.45;color:var(--white)}
  .service-list li::before{content:"• "}
  .ot-copy{position:absolute;left:36px;top:250px;width:320px}
  .italic .panel-title,.italic .service-list,.italic .lead{font-style:italic}
  .speech-copy{position:absolute;left:20px;top:190px;width:345px}
  .speech-copy .panel-title,.speech-copy .lead{text-align:center}
  .speech-copy .service-list{font-weight:700;font-size:12.5px;line-height:1.45;white-space:nowrap}
  .sensory-block{margin-top:14px}
  .sensory-block .service-list{font-weight:400;font-size:12.5px;line-height:1.5}
  .panel--grey{background:var(--panel-grey);border-left:16px solid var(--orange);border-right:16px solid var(--orange)}
  .cap{position:absolute;left:0;right:0;background:var(--navy)}
  .cap--top{top:0;height:84px;border-radius:0 0 60px 60px;display:flex;align-items:center;justify-content:center}
  .cap--top .cap-title{color:var(--white);font-weight:700;font-size:26px}
  .cap--bottom{bottom:0;height:96px;border-radius:110px 110px 0 0;display:flex;align-items:center;justify-content:center;gap:10px}
  .brand-dot{width:14px;height:14px;border-radius:50%;background:var(--white)}
  .brand-name{color:var(--white);font-weight:700;font-size:19px;line-height:1.15;text-align:center}
  .grey-copy{position:absolute;left:18px;right:16px;top:98px;color:var(--text-dark)}
  .grey-copy .lead{color:#3a3a3a;text-align:center;font-size:12.5px;line-height:1.35;margin:4px 0 8px}
  .grey-copy .service-list{color:var(--text-dark);font-weight:700;font-size:13px;line-height:1.35;white-space:nowrap}
  .grey-title{color:var(--navy);font-weight:700;font-size:26px;line-height:1.1;text-align:center;margin-top:14px}
</style>
</head>
<body>
<main class="brochure">

  <section class="panel panel--blue">
    <svg class="photo" style="left:0;top:0" width="380" height="230" viewBox="0 0 380 230" role="img" aria-label="Photo of a smiling child with paint-covered hands and face">
      <defs><linearGradient id="paintGrad" x1="0" y1="0" x2="1" y2="1"><stop offset="0" stop-color="#f3ede6"/><stop offset=".5" stop-color="#e7b9a4"/><stop offset="1" stop-color="#f5f1ec"/></linearGradient></defs>
      <path d="M0 0H380V190Q340 215 300 200Q260 185 230 210Q190 232 150 205Q110 185 70 205Q35 222 0 200Z" fill="url(#paintGrad)"/>
    </svg>
    <div class="ot-copy">
      <h2 class="panel-title">Occupational Therapy</h2>
      <p class="lead">Helping children build better self-esteem, confidence and independence in all the things they do.</p>
      <ul class="service-list">
        <li>Sensory Processing Disorder</li>
        <li>Balance, Coordination, Strength, and Endurance</li>
        <li>Fine Motor and Handwriting</li>
        <li>Visual- Motor Integration</li>
        <li>Play and Social Skills</li>
        <li>Feeding and Oral Motor Skills</li>
        <li>Self-Care</li>
        <li>Academic and Cognitive Skills</li>
        <li>Behavioral Difficulties</li>
        <li>Developmental Delays</li>
      </ul>
    </div>
    <svg class="photo" style="left:0;top:640px" width="380" height="240" viewBox="0 0 380 240" role="img" aria-label="Photo of a child playing on a pink therapy ball">
      <defs><linearGradient id="ballGrad" x1="0" y1="0" x2="1" y2="1"><stop offset="0" stop-color="#f4f1ea"/><stop offset=".45" stop-color="#a9c96a"/><stop offset="1" stop-color="#e6357f"/></linearGradient></defs>
      <path d="M0 40Q40 10 80 30Q130 55 170 25Q220 0 260 40Q300 75 330 120Q360 170 380 240H0Z" fill="url(#ballGrad)"/>
    </svg>
  </section>

  <section class="panel panel--blue italic">
    <svg class="photo" style="left:200px;top:24px" width="156" height="156" viewBox="0 0 156 156" role="img" aria-label="Photo of three children whispering to each other">
      <defs><linearGradient id="kidsGrad" x1="0" y1="0" x2="1" y2="0"><stop offset="0" stop-color="#e9c7a8"/><stop offset=".5" stop-color="#a6785a"/><stop offset="1" stop-color="#3f4f70"/></linearGradient></defs>
      <circle cx="78" cy="78" r="76" fill="url(#kidsGrad)" stroke="#ffffff" stroke-width="3"/>
    </svg>
    <div class="speech-copy">
      <h2 class="panel-title">Speech Therapy</h2>
      <p class="lead">Helping children speak, communicate and understand language.</p>
      <ul class="service-list">
        <li>Expressive and Receptive Language</li>
        <li>Speech and Language Developmental Milestones</li>
        <li>Articulation / Intelligibility</li>
        <li>Speech Fluency</li>
        <li>Pragmatics and Social Skills</li>
        <li>Literacy and Vocabulary</li>
        <li>Apraxia of Speech</li>
        <li>Augmentative and Alternative Communication</li>
        <li>Feeding and Oral Motor</li>
      </ul>
      <div class="sensory-block">
        <h2 class="panel-title">Sensory Integration</h2>
        <p class="lead">Gradually increasing play based activities to improve a child's nervous system. Helping children learn to self-regulate their emotions, behaviors and arousal levels.</p>
        <ul class="service-list">
          <li>Autism and ADHD</li>
          <li>Sensory Processing Disorder</li>
          <li>Poor Tolerance of Sensory Stimuli from the Environment</li>
          <li>Meltdowns and Tantrums</li>
          <li>Poor Balance/Body Awareness</li>
          <li>Poor Attention and Concentration</li>
          <li>Poor Self-Regulation</li>
          <li>Behavior and Social Difficulties</li>
          <li>Poor Motor Coordination and Motor Planning</li>
          <li>Aggression, Frustration or Avoidance Behaviors</li>
        </ul>
      </div>
    </div>
  </section>

  <section class="panel panel--grey">
    <div class="cap cap--top"><h2 class="cap-title">Sensory Integration</h2></div>
    <div class="grey-copy">
      <p class="lead">Providing skilled assessment and intervention to children with feeding difficulties.</p>
      <ul class="service-list">
        <li>Food Aversions</li>
        <li>Food Refusal</li>
        <li>Very Picky Eating</li>
        <li>Avoidance of Certain Textures</li>
        <li>Gagging and Vomiting</li>
        <li>Oral Motor/ Chewing Difficulties</li>
        <li>Limited Diet/Food Repertoire</li>
      </ul>
      <h2 class="grey-title">Physical Therapy</h2>
      <p class="lead">Helping children move and interact within their environment smoothly and confidently.</p>
      <ul class="service-list">
        <li>Torticollis</li>
        <li>Walking and Mobility</li>
        <li>Developmental Motor Milestones</li>
        <li>Balance, Coordination, Motor Planning</li>
        <li>Strength, Muscle Tone and Range of Motion</li>
        <li>Sports Injuries</li>
        <li>Toe Walking</li>
        <li>Myofascial Release</li>
        <li>Postural Control and Positioning</li>
      </ul>
      <h2 class="grey-title">Group Therapy</h2>
      <p class="lead">Using peer role models to learn new and challenging skills.</p>
      <ul class="service-list">
        <li>Social Groups</li>
        <li>Feeding Groups</li>
      </ul>
      <p class="service-list">**More Group Classes Coming Soon</p>
    </div>
    <div class="cap cap--bottom">
      <span class="brand-dot"></span>
      <span class="brand-name">Clearbrook<br>Pediatric Therapy</span>
    </div>
  </section>

</main>
</body>
</html>
```